Customizable Form Generation Website

This will be a place for users to quickly generate numerous forms from a categorized list. As the forms are templates with field variables, the site must be able to substitute ‘real data’ for template variable data. This tool will allow for quick custom forms on-demand.

The landing page is attached. We need the User Experience and User Interface solved for us.

EXAMPLE:
——————————————————————-
Dear {{PatientFirstName}},

Please come back for an examination on {{SelectedDate}} with Doctor {{SelectedProvider}}.

Sincerely,

{{SelectedAuthor}}
——————————————————————-

Coming to the Forms Landing Page, the user will see the forms available to select. The user will then click to select a form.

At some point, the user must resolve the variables in the form. For instance, there are the following variables in the above example: PatientFirstName, SelectedDate, SelectedProvider, and SelectedAuthor. We must give the user a chance to select the values for these variables. Using a dropdown combobox will probably work for most. Getting a date selector will be required if the variable happens to contain the string 'date'.

Is it best to preselect common variables before opening the form, or is it best to dynamically scan the template, then give the user the option to give values to each variable found?

The design must include a way for users to upload additional forms. Forms will most probably be PDF, .DOC, .TXT files. This allows users to develop simple or fancy forms of their choosing., then simply drop them into the site for future use.

The design must include a way for users to create new forms. The form creation tool must present to the user the list of predefined variables like {{PatientLastName}} for easy insertion into the form writer. Anytime "{{}}" are used, developers will recognize that as a variable that needs to be resolved.

The forms will be separated into categories as follows:

OFFICE:
- Letterhead
- Sign-In Sheet
- Fax Cover Sheet
SCHEDULER:
- Appointment Reminder
- Missed Appointment Policy
PATIENT:
- Intake Form
- Patient Discharge
- Return to Work or School
- Excuse Slip
- Consent to Treat a Minor
- Verify Non-Pregnancy
RELEASE:
- Health Information Release Form
- X-Ray Release Form
CERTIFICATES:
- Certificate of Care
- Disability Certificate
INSURANCE:
- Authorization to Bill Insurance
- Assignment Authorization
OTHER:
- Free Massage
- Free Vitamins

The design must include a way to add/customize categories. Categories are for organizing the forms logically.

We welcome ANY questions to help understand the requirements.

Good luck!

Industry/Entity Type

Healthcare

Number of Pages Required

3 page

Requirements
Must have
• Must Follow ORBITAL SCHEMA standards
Nice to have
• Great User Experience. Simple, Fast, Clever.
Should not have
• nothing to add here

```html
<!DOCTYPE html>
<html lang="en">
<head>
<meta charset="utf-8">
<title>FormHarbor – Our Template</title>
<link href="https://fonts.googleapis.com/css2?family=Rubik:wght@400;500&display=swap" rel="stylesheet">
<style>
  :root {
    --navy: #0d1b2a;
    --ink: #14202e;
    --muted: #8a9098;
    --accent: #1a5b94;
    --panel: #f5f5f5;
    --divider: #e6e6e6;
    --white: #ffffff;
  }
  * { box-sizing: border-box; margin: 0; padding: 0; }
  html, body { width: 1200px; height: 606px; overflow: hidden; background: var(--white); }
  body { font-family: "Rubik", sans-serif; color: var(--ink); position: relative; }

  .topbar { height: 50px; background: var(--navy); color: var(--white); display: flex; align-items: center; padding: 0 159px; }
  .brand { font-size: 15px; font-weight: 500; letter-spacing: -0.2px; }
  .topnav { margin-left: auto; display: flex; align-items: center; gap: 22px; font-size: 10px; }
  .topnav span { display: flex; align-items: center; gap: 5px; }
  .topnav svg { width: 13px; height: 13px; stroke: var(--white); fill: none; stroke-width: 1.1; }

  .page-title { position: absolute; left: 159px; top: 79px; font-size: 20px; font-weight: 400; }
  .btn-create { position: absolute; left: 904px; top: 75px; width: 137px; height: 35px; background: var(--accent); color: var(--white); border: none; font: 500 10px "Rubik", sans-serif; }

  .sidebar { position: absolute; left: 159px; top: 132.5px; width: 207px; background: var(--panel); }
  .cat { height: 47px; border-top: 1px solid var(--divider); display: flex; align-items: center; justify-content: space-between; padding: 0 18px 0 17.5px; font-size: 12.5px; font-weight: 500; }
  .cat .toggle { font-size: 12px; font-weight: 500; }
  .cat.open { height: 111px; border-top: none; flex-direction: column; align-items: stretch; justify-content: flex-start; padding-top: 14px; position: relative; }
  .cat.open::before { content: ""; position: absolute; left: 0; top: 14px; width: 2px; height: 19px; background: var(--accent); }
  .cat-head { display: flex; justify-content: space-between; align-items: center; height: 19px; font-weight: 400; }
  .cat-items { list-style: none; margin-top: 9px; font-size: 9.5px; font-weight: 400; }
  .cat-items li { height: 20px; line-height: 20px; }
  .cat-items li.current { text-decoration: underline; }

  .btn-custom { position: absolute; left: 159px; top: 539px; width: 207px; height: 35px; background: var(--white); border: 1px solid var(--navy); font: 500 10px "Rubik", sans-serif; color: var(--ink); }

  .templates { position: absolute; left: 384px; top: 132.5px; display: grid; grid-template-columns: repeat(4, 151px); column-gap: 17.5px; row-gap: 17.5px; }
  .card { height: 215.6px; }
  .thumb { height: 101px; }
  .thumb.smoke { background: radial-gradient(ellipse at 55% 45%, #6f9fb4 0%, #1f4a5c 30%, #050a0e 65%); }
  .thumb.cabin { background: linear-gradient(180deg, #d9dde0 0%, #7c8a6e 40%, #c4c9cc 60%, #5b6a46 100%); }
  .thumb.glass { background: radial-gradient(circle at 55% 40%, #f05a14 0%, #d4361a 30%, #2a52b8 65%, #e8a11a 100%); }
  .thumb.spiral { background: radial-gradient(circle at 50% 30%, #2e2e2e 0%, #e6e6e6 12%, #cfcfcf 55%, #8e8e8e 100%); }
  .card h3 { font-size: 12.5px; font-weight: 400; margin-top: 12px; }
  .card p { font-size: 9.5px; line-height: 15px; color: var(--muted); margin-top: 5px; width: 140px; }
  .use { display: inline-flex; align-items: center; gap: 4px; font-size: 10px; font-weight: 500; margin-top: 6px; }
  .use svg { width: 9px; height: 7px; stroke: var(--ink); fill: none; stroke-width: 1.2; }
</style>
</head>
<body>
  <header class="topbar">
    <div class="brand">FormHarbor</div>
    <nav class="topnav">
      <span><svg viewBox="0 0 14 14"><rect x="1" y="4" width="8" height="9"/><rect x="9" y="7" width="4" height="6"/><path d="M3 6h1M6 6h1M3 9h1M6 9h1"/></svg>Sample healthcare practice</span>
      <span><svg viewBox="0 0 14 14"><circle cx="7" cy="7" r="6"/><circle cx="7" cy="6" r="2"/><path d="M3.5 11c1-2 6-2 7 0"/></svg>Welcome back test</span>
      <span><svg viewBox="0 0 14 14"><path d="M9 1h4v12H9M1 7h8M6 4l3 3-3 3"/></svg>Log out</span>
    </nav>
  </header>

  <h1 class="page-title">Our Template</h1>
  <button class="btn-create">Create From</button>

  <aside class="sidebar">
    <div class="cat open">
      <div class="cat-head"><span>Office</span><span class="toggle">–</span></div>
      <ul class="cat-items">
        <li class="current">Letterhead</li>
        <li>Sign-In Sheet</li>
        <li>Fax Cover Sheet</li>
      </ul>
    </div>
    <div class="cat"><span>Scheduler</span><span class="toggle">+</span></div>
    <div class="cat"><span>Patient</span><span class="toggle">+</span></div>
    <div class="cat"><span>Release</span><span class="toggle">+</span></div>
    <div class="cat"><span>Certificates</span><span class="toggle">+</span></div>
    <div class="cat"><span>Insurance</span><span class="toggle">+</span></div>
    <div class="cat"><span>Other</span><span class="toggle">+</span></div>
  </aside>
  <button class="btn-custom">Add custom form</button>

  <main class="templates">
    <article class="card"><div class="thumb smoke" role="img" aria-label="Blue smoke on a black background"></div><h3>Letterhead forms</h3><p>But I must explain to you how all this mistaken idea of denouncing</p><span class="use">Use Template <svg viewBox="0 0 9 7"><path d="M0 3.5h8M5 0.5l3 3-3 3"/></svg></span></article>
    <article class="card"><div class="thumb cabin" role="img" aria-label="White A-frame cabin among trees"></div><h3>Letterhead forms</h3><p>But I must explain to you how all this mistaken idea of denouncing</p><span class="use">Use Template <svg viewBox="0 0 9 7"><path d="M0 3.5h8M5 0.5l3 3-3 3"/></svg></span></article>
    <article class="card"><div class="thumb glass" role="img" aria-label="Colourful blown glass art"></div><h3>Letterhead forms</h3><p>But I must explain to you how all this mistaken idea of denouncing</p><span class="use">Use Template <svg viewBox="0 0 9 7"><path d="M0 3.5h8M5 0.5l3 3-3 3"/></svg></span></article>
    <article class="card"><div class="thumb spiral" role="img" aria-label="White spiral staircase seen from below"></div><h3>Letterhead forms</h3><p>But I must explain to you how all this mistaken idea of denouncing</p><span class="use">Use Template <svg viewBox="0 0 9 7"><path d="M0 3.5h8M5 0.5l3 3-3 3"/></svg></span></article>
    <article class="card"><div class="thumb glass" role="img" aria-label="Colourful blown glass art"></div><h3>Letterhead forms</h3><p>But I must explain to you how all this mistaken idea of denouncing</p><span class="use">Use Template <svg viewBox="0 0 9 7"><path d="M0 3.5h8M5 0.5l3 3-3 3"/></svg></span></article>
    <article class="card"><div class="thumb spiral" role="img" aria-label="White spiral staircase seen from below"></div><h3>Letterhead forms</h3><p>But I must explain to you how all this mistaken idea of denouncing</p><span class="use">Use Template <svg viewBox="0 0 9 7"><path d="M0 3.5h8M5 0.5l3 3-3 3"/></svg></span></article>
  </main>
</body>
</html>
```